Leading Technology Rental Company Need a graphic design to put on homepage

We need a graphic design for a new webpage for our company - Plover Rentals. We specialize in the technology rental for Convention/Trade shows/Compnay Events/Training/Weddings/.... Looking to create a new graphic design for a landing page which will project the right image and message.

new webpage in progress http://www.ploverrentalsbay.example/home

Looking to replace the rotating equipment images with a single image that will project best-in-class equipment/services/reliable. image also need to include a bold message statement.

```html
<!DOCTYPE html>
<html lang="en">
<head>
<meta charset="utf-8">
<title>Home - Plover Rentals</title>
<link rel="stylesheet" href="https://fonts.googleapis.com/css2?family=Jost:wght@300;400;500;700&display=swap">
<style>
  :root {
    --page-bg: #ffffff;
    --ink: #2b2b2b;
    --ink-soft: #3a3a3a;
    --muted: #555555;
    --teal: #1d6a6e;
    --teal-dark: #0f6663;
    --white: #ffffff;
  }
  * { margin: 0; padding: 0; box-sizing: border-box; }
  html, body {
    width: 1200px;
    height: 1000px;
    overflow: hidden;
    background: var(--page-bg);
    font-family: "Jost", "Futura", sans-serif;
    color: var(--ink);
  }
  .page { position: relative; width: 1200px; height: 1000px; }

  .site-header { position: absolute; top: 0; left: 0; width: 1200px; height: 110px; }
  .brand {
    position: absolute; left: 105px; top: 32px;
    display: flex; align-items: center; gap: 10px;
  }
  .brand-square { width: 14px; height: 14px; background: var(--teal); flex: none; }
  .brand-name {
    font-size: 22px; font-weight: 500; color: var(--teal);
    white-space: nowrap; line-height: 1;
  }

  .main-nav {
    position: absolute; top: 37px; right: 232px;
    display: flex; gap: 14px;
    font-size: 13px; font-weight: 400; color: var(--ink);
    letter-spacing: 0.2px;
  }
  .phone-button {
    position: absolute; top: 27px; left: 981px; width: 130px; height: 37px;
    background: var(--teal-dark); color: var(--white);
    display: flex; align-items: center; justify-content: center;
    font-size: 15px; letter-spacing: 0.4px;
  }

  .hero-headline {
    position: absolute; left: 175px; top: 158px;
    font-size: 48px; font-weight: 700; line-height: 54px;
    color: var(--ink); letter-spacing: 0.5px;
  }
  .hero-subline {
    position: absolute; left: 175px; top: 362px;
    font-size: 25px; font-weight: 300; line-height: 34px; color: var(--ink-soft);
  }
  .hero-equipment {
    position: absolute; left: 607px; top: 168px; width: 406px; height: 261px;
  }

  .reassurance-title {
    position: absolute; top: 496px; left: 0; width: 1200px; text-align: center;
    font-size: 36px; font-weight: 300; color: var(--teal); letter-spacing: 0.5px;
  }
  .reassurance-copy {
    position: absolute; top: 570px; left: 0; width: 1200px; text-align: center;
    font-size: 14px; font-weight: 300; line-height: 31px; color: var(--muted);
  }
</style>
</head>
<body>
<div class="page">
  <header class="site-header">
    <div class="brand">
      <span class="brand-square"></span>
      <span class="brand-name">Plover Rentals</span>
    </div>
    <nav class="main-nav">
      <span>SOLUTIONS</span><span>RENTALS</span><span>ABOUT</span><span>CAREER</span><span>CONTACT</span><span>REQUEST A QUOTE</span>
    </nav>
    <div class="phone-button">800-555-0142</div>
  </header>

  <h1 class="hero-headline">KNOWLEDGE.<br>EXPERIENCE.<br>RESULTS.</h1>
  <p class="hero-subline">High-tech office equipment<br>for your next business event</p>

  <svg class="hero-equipment" viewBox="0 0 406 261" role="img" aria-label="Group of rental equipment: desktop tower, laptop, tablet and a large flat-screen display">
    <defs>
      <linearGradient id="equipTone" x1="0" y1="0" x2="1" y2="1">
        <stop offset="0" stop-color="#e4e6e9"/>
        <stop offset="0.55" stop-color="#b9bcc2"/>
        <stop offset="1" stop-color="#2a2a2e"/>
      </linearGradient>
    </defs>
    <rect width="406" height="261" rx="6" fill="url(#equipTone)"/>
  </svg>

  <h2 class="reassurance-title">YOU CAN COUNT ON US...</h2>
  <p class="reassurance-copy">Whether you are holding a tradeshow, hotel convention, or any type of business meeting in the Las Vegas, NV or<br>San Francisco, CA region, you can always count on Plover Rentals. By combining premium AV rental</p>
</div>
</body>
</html>
```